Visitenkarte für Ergotherapiepraxis
Zielgruppe
Wir arbeiten mit Kindern und Erwachsene jeden Alters.
Diese Personen kommen mit Beeinträchtigungen (körperlich, seelisch, schulisch) im täglichen Leben zu uns. Wir unterstützen unsere Patienten die Beeinträchtigungen zu verringern oder zu kompensieren und so den Alltag besser bewältigen zu können.
Aufgabenstellung
Ein Design was Kinder und Erwachsene anspricht, aber nicht zu verspielt wirkt. Es soll vertrauenserweckend sein. Eventuell sollte die Visitenkarte ein "aufgehendes oder erblühendes oder aufsteigendes" Element enthalten (=zu Beginn war die Beeinträchtigung dann steigt die Lebensqualität als Folge der Behandlung)
Daten vorn:
Ergotherapiepraxis

```html
<!DOCTYPE html>
<html lang="de">
<head>
<meta charset="utf-8">
<title>Visitenkarte Ergotherapiepraxis – Rückseite</title>
<link rel="stylesheet" href="https://fonts.googleapis.com/css2?family=Arimo:wght@400&display=swap">
<style>
  :root {
    --band-sand: #e5dca6;
    --ink-navy: #15246b;
    --blossom-coral: #f07a5f;
    --blossom-pink: #e8c9d6;
    --leaf-grey: #8a9a96;
    --mist-white: #efe6ee;
  }
  html, body {
    margin: 0;
    padding: 0;
    width: 1200px;
    height: 695px;
    overflow: hidden;
    background: var(--band-sand);
  }
  .card {
    position: relative;
    width: 1200px;
    height: 695px;
    overflow: hidden;
  }
  .therapist-band {
    height: 296px;
    background: var(--band-sand);
    display: flex;
    align-items: center;
    justify-content: center;
  }
  .therapist-info {
    margin: 12px 0 0 10px;
    text-align: center;
    font-family: "Arimo", Arial, sans-serif;
    font-size: 39px;
    line-height: 51px;
    color: var(--ink-navy);
  }
  .therapist-role,
  .therapist-name {
    display: block;
  }
  .blossom-photo {
    height: 399px;
    background:
      radial-gradient(ellipse 30% 40% at 45% 40%, rgba(240, 122, 95, 0.75), transparent 70%),
      radial-gradient(ellipse 25% 35% at 80% 55%, rgba(240, 122, 95, 0.7), transparent 70%),
      radial-gradient(ellipse 20% 30% at 20% 70%, rgba(240, 122, 95, 0.65), transparent 70%),
      linear-gradient(160deg, var(--mist-white) 0%, var(--blossom-pink) 35%, var(--leaf-grey) 70%, var(--blossom-pink) 100%);
  }
</style>
</head>
<body>
  <main class="card">
    <section class="therapist-band">
      <p class="therapist-info">
        <span class="therapist-role">Behandelnder Therapeut:</span>
        <span class="therapist-name">Lena Marwitz</span>
      </p>
    </section>
    <div class="blossom-photo" role="img" aria-label="Foto eines blühenden Zweigs mit korallroten Blüten vor unscharfem rosa-grauem Hintergrund"></div>
  </main>
</body>
</html>
```